Coffee Company 1lb coffee bag design

Coffee Bag Design Size ( bag size 12 -16oz / 340 -454 grams / 1lb - dimensions) THE BAG IS GUSSETTED - meaning it has 4sides , like the bags shown in the attachments

* recommend text located at the bottom of the brief added July 9 th

We need a design for a retail 1lb coffee bag to package our Artisan handcrafted roasted coffee beans. The design we choose will be the standard 'look' for our freshly roasted coffee. We have our logo and need to incorporate that into an original, overall design that includes areas for text boxes on the front, back and sides. We have provided a draft of the text at the bottom of the brief to be incorporated in the design. One text box on the front will remain blank. This is where we will adhere a label that will describe the particular coffee in the package. And blank text box on the back to print a bar code.
(Side of the bag : one side of the bag would be our company story (details can be found on our web site) and the other side panel brewing instruction. I would be able to provide the txt for the 'story' and 'brewing instructions' as needed)

These are our preliminary thoughts and are open minded to other options.
We want the design to convey that our coffee is an ethically sourced , locally hand roasted in small batches , freshly roasted, sustainable, socially and environmentally responsible.

This bag will be the our main core bag for use with all the Blends / Roasts so it will need to be starting point for our overall bag design branding. We are very open to all and any creative ideas..
Ideally we would like to use a crisp white gloss bag - the logo would be the main focal point with an area below for where we would place our sticker - roast / blend details .we will be to using a sticker on the front of the bag to identify the various roasts / blends we offer until a point of having a different bag for each coffee. We don't want the bag the appear 'busy' as we prefer images over covering the whole bag with a photo.. the design needs to be crisp , clean , not overall busy, classy , using inspiration perhaps from the logo , twin ridge mountain range , blue ocean, green trees .... our customers enjoy the finer things in life and our brand is more of a luxury product.
Who we are:
We are a Artisan coffee roaster located in the village of Fernhollow. Our hand crafted roasted coffee is ethically sourced , locally roasted in small batches to ensure freshness in every cup. please check out our web site for further details on the company. Again , we are open and looking forward to seeing some fantastic core bag design. we will be looking for the opportunity to develop stickers for each blends in the future...

www.fernhollowcoffeeco.example

attached is the logo files and other bags that have caught our interest ... have some fun!

TEXT FOR: SIDE #1, SIDE #2 , BACK OF THE BAG

FYI - this text is still currently in DRAFT but will allow us to get an overall look for each design...

One side of the coffee bag

Revised draft of the text - updated July19th

THE STORY OF

THE FERNHOLLOW

COFFEE COMPANY,

Nestled beneath the two majestic peaks of the Twin Ridge Mountains along the scenic Cedar Crest highway, is the picturesque village of Fernhollow. This small waterfront community on Vancouver’s North Shore boasts a synchronicity between snowcapped mountains that feed twinkling creeks which meander through lush green forests and lead to the beautiful ocean. This was our inspiration to create Fernhollow Coffee Company and to share our passion for the perfect cup of coffee as reflected in each of our roasts. Our artisan roasted coffee is ethically sourced, using the highest quality Arabica beans then locally roasted in small batches to ensure freshness and the finest flavor. May the coffee you are about to enjoy, enhance your day as you experience the essence of Fernhollow.

-------------------------------------------------

Fernhollow Coffee Company

PO BOX 482

Fernhollow BC

V0K 3R5

the other Side of Bag

KEYS TO BREWING

THE PERFECT CUP

FRESHNESS

Always use freshly roasted (Fernhollow Coffee Company)

beans and within 1-2 weeks of purchase.

STORING

Your coffee has 4 enemies:

Heat, Moisture, Light & Air

Keep your coffee cool, dry and dark in an

airtight container for maximum flavour.

GRINDING

Grind beans just before

brewing. Select the best

grind for each brewing method:

Espresso = Finer Grind

Filtered = Medium Grind

French Press = Coarse Grind

BREWING

Water I Ratio I Temperature

Water: Fresh, cold, filtered water

Ratio: Use 2 rounded tablespoons

of coffee per 8 oz of water.

Temperature: Heat water between 90 – 96 C

Adjust brewing methods to your personal taste.

For more information about

brewing the perfect cup of coffee,

visit our website at

www.fernhollowcoffeeco

(ADD RGBT logo - to be provided)

Back of the bag

"The roasts I create for Fernhollow Coffee Company are a reflection of my commitment to craft the perfect cup of coffee. I hope it is the finest coffee you'll ever enjoy."
- Doran Pettifer,
Founder & Master Roaster, Fernhollow Coffee Company

Visit us our website to learn more including ordering your freshly roasted coffees

(ADD miniature Fernhollow Coffee Company logo)

Like us on Chirpbook

htpp://www.socialpage.example/fernhollowcoffeeco

Follow us on Tweetle

Fernhollow Coffee @fernhollowbrew

send us an email

info@fernhollowcoffeeco.example
Updates

Design Team, just a reminder the bag design is for a gusseted bag ( see brief for details and images ) and not for a pouch bag as what is being submitted to me ? All current designs received so far are the wrong style of bag.

Update effective July 19th, 2014. Please see Brief for revised text for Keys to Brewing, The Story and back side of bag. Thanks.

Reason: Still working with a few designers with text and design - need more time Starting to narrow our selection down soon

Reason: Need to extend to add French to package design

Target Market(s)

coffee drinkers with a mature palate for Arabica Beans , ethically sourced

Industry/Entity Type

It Company

Font styles to use
Other font styles liked:
• same font as logo ?

Colors
0893cd
33a6d7
85cae6
85acd3
3176b5
0455a3
ffffff
cee9f5
eaf1f6

Requirements
Must have
• logo is the main image on front of bag , space for the sticker that will describe the type of bean / roast / blend
Nice to have
• white bag , logo has strong presents front and middle of the bag. crisp clean not busy designs
Should not have
• package should not be 'too busy' it is the core for all roasts and should stand for the roasting company

no cartoon pictures and un authorized clip art

```html
<!DOCTYPE html>
<html lang="en">
<head>
<meta charset="utf-8">
<title>Fernhollow Coffee Company – 1lb Gusseted Bag Dieline</title>
<link href="https://fonts.googleapis.com/css2?family=Open+Sans:ital,wght@0,400;0,600;0,700;1,400&family=Oswald:wght@300;400&display=swap" rel="stylesheet">
<style>
  :root {
    --band-blue: #4587bd;
    --navy: #1d4f8f;
    --brand-blue: #2a6aae;
    --text-grey: #6b6b6b;
    --rule-grey: #9a9a9a;
    --mist: #e3edf3;
    --paper: #ffffff;
    --ink: #111111;
    --logo-brown: #5a2e22;
  }
  * { margin: 0; padding: 0; box-sizing: border-box; }
  html, body { width: 1200px; height: 973px; overflow: hidden; background: var(--paper); }
  .dieline {
    position: relative; width: 1200px; height: 973px;
    font-family: "Open Sans", Arial, sans-serif; color: var(--text-grey);
  }
  .dieline__art { position: absolute; inset: 0; }
  .abs { position: absolute; }
  .center { text-align: center; }

  .panel-label {
    position: absolute; top: 7px; font-weight: 700; font-size: 16px; color: var(--ink);
    text-align: center; width: 200px; margin-left: -100px;
  }
  .seal-label {
    position: absolute; top: 879px; font-weight: 700; font-size: 16px; color: var(--ink);
    text-align: center; width: 240px; margin-left: -120px;
  }
  .seal-label--vertical {
    position: absolute; left: 1116px; top: 464px; width: 240px; margin-left: -120px; margin-top: -11px;
    transform: rotate(-90deg); text-align: center; font-weight: 700; font-size: 16px; color: var(--ink);
  }

  .brand-mark {
    position: absolute; width: 160px; margin-left: -80px; text-align: center;
  }
  .brand-mark__dot {
    width: 92px; height: 92px; border-radius: 50%; background: var(--logo-brown);
    margin: 0 auto 10px;
  }
  .brand-mark__name {
    font-family: "Oswald", sans-serif; font-weight: 400; font-size: 26px; letter-spacing: 1px;
    color: var(--logo-brown); line-height: 1;
  }

  .tagline {
    position: absolute; font-family: "Oswald", sans-serif; font-weight: 300;
    font-size: 17px; letter-spacing: 2px; color: var(--navy); text-align: center;
  }

  .back-copy { position: absolute; left: 100px; width: 295px; text-align: center; }
  .back-copy p { font-size: 10.5px; line-height: 15px; }
  .back-copy .muted { font-weight: 600; color: var(--text-grey); }
  .back-copy .link { font-weight: 700; color: var(--navy); }
  .back-copy .url { font-weight: 700; font-size: 13px; color: var(--navy); }

  .side-heading {
    position: absolute; text-align: center; font-weight: 700; font-size: 12px;
    line-height: 14.5px; color: var(--brand-blue); letter-spacing: 0.3px;
  }
  .story {
    position: absolute; left: 432px; width: 132px; font-style: italic;
    font-size: 7.4px; line-height: 10.5px; color: var(--brand-blue); letter-spacing: 0.15px;
  }
  .story p + p { margin-top: 10px; }
  .address {
    position: absolute; left: 395px; width: 204px; text-align: center;
    font-weight: 700; font-size: 9px; line-height: 11px; color: var(--navy); letter-spacing: 0.3px;
  }
  .address .web { margin-top: 9px; font-size: 8.5px; }

  .sticker-area {
    position: absolute; left: 636px; top: 316px; width: 220px; height: 201px;
    border: 1px dashed #b9b9b9; border-radius: 8px;
    display: flex; align-items: center; justify-content: center; text-align: center;
    font-size: 16px; line-height: 20px; color: #a9a9a9;
  }
  .net-weight {
    position: absolute; left: 815px; top: 699px; font-family: "Oswald", sans-serif;
    font-weight: 300; font-size: 17px; color: #3a3a3a;
  }

  .brewing { position: absolute; left: 921px; width: 150px; }
  .brewing h3 { font-size: 10.5px; font-weight: 700; color: var(--navy); line-height: 13px; margin-top: 3px; }
  .brewing p { font-size: 7.3px; line-height: 9px; color: var(--text-grey); }
  .brewing p + p { margin-top: 8px; }
  .brewing-footer {
    position: absolute; left: 892px; width: 205px; text-align: center;
    font-weight: 700; font-size: 7.8px; line-height: 10px; color: var(--navy);
  }
  .brewing-footer .web { margin-top: 10px; }
</style>
</head>
<body>
<main class="dieline">

  <svg class="dieline__art" width="1200" height="973" viewBox="0 0 1200 973" aria-hidden="true">
    <defs>
      <linearGradient id="mist-fade" x1="0" y1="0" x2="0" y2="1">
        <stop offset="0" stop-color="#e3edf3" stop-opacity="0.55"/>
        <stop offset="0.12" stop-color="#e3edf3" stop-opacity="1"/>
        <stop offset="1" stop-color="#e3edf3"/>
      </linearGradient>
    </defs>
    <!-- outer frame -->
    <rect x="100.5" y="34.5" width="1033" height="905" fill="#fff" stroke="#8a8a8a"/>
    <!-- top band -->
    <rect x="101" y="35" width="1032" height="35" fill="var(--band-blue)"/>
    <!-- seal strip blue -->
    <rect x="1097" y="758" width="36" height="181" fill="var(--band-blue)"/>
    <!-- side panel lower fills -->
    <rect x="395" y="758" width="204" height="98" fill="#f1f6f9"/>
    <rect x="892" y="758" width="205" height="98" fill="#f1f6f9"/>
  </svg>

  <svg class="abs" style="left:101px;top:300px" width="294" height="556" viewBox="0 0 294 556" role="img" aria-label="Faint snow-capped twin ridge mountain backdrop">
    <rect width="294" height="556" fill="url(#mist-fade)"/>
  </svg>
  <svg class="abs" style="left:599px;top:590px" width="293" height="266" viewBox="0 0 293 266" role="img" aria-label="Faint snow-capped mountain backdrop">
    <defs>
      <linearGradient id="mist-fade-front" x1="0" y1="0" x2="0" y2="1">
        <stop offset="0" stop-color="#e3edf3" stop-opacity="0.4"/>
        <stop offset="0.3" stop-color="#e3edf3"/>
        <stop offset="1" stop-color="#e3edf3"/>
      </linearGradient>
    </defs>
    <rect width="293" height="266" fill="url(#mist-fade-front)"/>
  </svg>

  <svg class="dieline__art" width="1200" height="973" viewBox="0 0 1200 973" aria-hidden="true">
    <g stroke="var(--rule-grey)" stroke-width="1" stroke-dasharray="4 3" fill="none">
      <line x1="395.5" y1="35" x2="395.5" y2="939"/>
      <line x1="599.5" y1="35" x2="599.5" y2="939"/>
      <line x1="892.5" y1="35" x2="892.5" y2="939"/>
      <line x1="1097.5" y1="35" x2="1097.5" y2="939"/>
      <line x1="101" y1="758.5" x2="1133" y2="758.5"/>
      <line x1="101" y1="856.5" x2="1133" y2="856.5"/>
      <polyline points="397,760 497,856 597,760"/>
      <polyline points="894,760 994,856 1095,760"/>
    </g>
  </svg>

  <div class="panel-label" style="left:250px">BACK</div>
  <div class="panel-label" style="left:497px">SIDE</div>
  <div class="panel-label" style="left:745px">FRONT</div>
  <div class="panel-label" style="left:993px">SIDE</div>

  <!-- BACK -->
  <div class="brand-mark" style="left:248px;top:130px">
    <div class="brand-mark__dot"></div>
    <div class="brand-mark__name">FERNHOLLOW</div>
  </div>
  <div class="tagline" style="left:100px;width:295px;top:279px">ARTISAN ROASTED COFFEE</div>
  <div class="back-copy" style="top:354px">
    <p class="muted">We hope that you will be inspired by our roasts<br>as much as we were are inspired to create them.</p>
    <p class="muted" style="margin-top:12px">Visit our website to learn more including<br>ordering your freshly roasted coffees</p>
    <p class="url" style="margin-top:12px">www.fernhollowcoffeeco.example</p>
    <p class="muted" style="margin-top:27px">Like us on Chirpbook</p>
    <p class="link" style="font-size:9.5px">http://www.socialpage.example/fernhollowcoffeeco</p>
    <p class="muted" style="margin-top:10px">Follow us on Tweetle</p>
    <p class="link">Fernhollow Coffee @fernhollowbrew</p>
    <p class="muted" style="margin-top:10px">send us an email</p>
    <p class="link">info@fernhollowcoffeeco.example</p>
  </div>

  <!-- SIDE: story -->
  <div class="side-heading" style="left:395px;width:204px;top:232px">THE STORY OF<br>THE FERNHOLLOW<br>COFFEE COMPANY</div>
  <div class="story" style="top:319px">
    <p>Nestled beneath the two majestic peaks of the Twin Ridge Mountains along the scenic Cedar Crest highway, is the picturesque village of Fernhollow. This small waterfront community on Vancouver's North Shore boasts a synchronicity between snowcapped mountains feeding twinkling creeks meandering through lush green forests and leading to the beautiful ocean.</p>
    <p>This was our inspiration to create the Fernhollow Coffee Company and to share our passion for the perfect cup of coffee as reflected in each of our roasts. Our Artisan coffee is ethically sourced, using the highest quality Arabica beans then locally roasted in small batches to ensure freshness and the finest flavor.</p>
    <p>May the coffee you are about to enjoy, enhance your day as you experience the essence of Fernhollow.</p>
  </div>
  <div class="address" style="top:658px">
    <div style="font-size:10px">Fernhollow Coffee Company</div>
    <div>PO BOX 482</div>
    <div>Fernhollow BC</div>
    <div>V0K 3R5</div>
    <div class="web">www.fernhollowcoffeeco.example</div>
  </div>

  <!-- FRONT -->
  <div class="brand-mark" style="left:745px;top:128px">
    <div class="brand-mark__dot"></div>
    <div class="brand-mark__name">FERNHOLLOW</div>
  </div>
  <div class="sticker-area">Sticker<br>area</div>
  <div class="tagline" style="left:599px;width:293px;top:533px">ARTISAN ROASTED COFFEE</div>
  <div class="net-weight">NET WT 1lb.</div>

  <!-- SIDE: brewing -->
  <div class="side-heading" style="left:892px;width:205px;top:237px">KEYS TO BREWING<br>THE PERFECT CUP</div>
  <div class="brewing" style="top:307px">
    <h3>Freshness</h3>
    <p>Always try to purchase your coffee at the peak of its freshness. For best results, purchase often and in smaller quantities (1-2 weeks supply max)</p>
    <h3>Storing</h3>
    <p>There are four enemies for your coffee: Oxygen, moisture, light and heat. So we keep your coffee dry, cool, dark and airtight for maximum taste</p>
    <h3 style="margin-top:8px">Grinding</h3>
    <p>Grind fresh just before brewing. Select the best grind for each brew method:</p>
    <p>Espresso = Finer Grind<br>Drip Coffees = Medium Grind<br>French Press Coffees = Coarse Grind</p>
    <h3 style="margin-top:5px">Brewing</h3>
    <p>Water: Fresh, cold, filtered water</p>
    <p style="margin-top:9px">Ratio: Use two rounded tablespoons of coffee per 8 oz of water. Adjust to to meet your personal needs.</p>
    <p>Temperature: Your water should be heated between 90 – 96 C</p>
    <p>Time: Use whatever method is right for you, some common methods:</p>
    <p>Espresso = 20-22 seconds<br>Pour Over = 2-3 minutes<br>French Press = 3-4 minutes<br>Auto Drip = 4-5 minute</p>
  </div>
  <div class="brewing-footer" style="top:690px">
    <div>For more information about<br>brewing the perfect cup of coffee<br>visit our website at</div>
    <div class="web">www.fernhollowcoffeeco</div>
  </div>

  <div class="seal-label--vertical">HEAT SEAL AREA</div>
  <div class="seal-label" style="left:246px">HEAT SEAL AREA</div>
  <div class="seal-label" style="left:499px">HEAT SEAL AREA</div>
  <div class="seal-label" style="left:746px">HEAT SEAL AREA</div>
  <div class="seal-label" style="left:997px">HEAT SEAL AREA</div>
</main>
</body>
</html>
```